business card for training & coaching company, Brightwell.co

Create a warm, clean, professional 2-sided business card for Brightwell.co.
Brightwell.co is a new company that shares Brightwell Dialogue (combination of mindfulness, kindness, and nonviolent communication), training and coaching individuals and groups.
Include the logo provided, perhaps incorporating a second opaque version of it as well.
Feelings & Needs lists on the reverse side of the card.

Target Market(s)

Women 30-60 years old, university educated.
Spiritual, may be Buddhist.

Industry/Entity Type

Training

Contact Information for Business Card

Marisabel T. Oberholt, MSc
Group Facilitator & Certified Wellness Coach
Brightwell Dialogue training & support
Group Facilitator & Coach
01632 960 418
07700 900 862
www.brightwell-example.co

Font styles to use
Sans Serif

Requirements
Must have
• Front -- Contact details, logo provided.
• Back -- Feelings list; Needs list
• Professional yet warm, inviting, friendly feel.
Nice to have
• little graphics (telephone for phone number, envelope for email, globe for web);
• Clean font (like Sathu, Frutiga, Helvetica).
• Feeling of movement or transformation.
Should not have
• More than 3 colours.
• Loud or busy designs.
• A gentle curve or two is ok, but not swirly designs.
• No black or other heavy backgrounds.

```html
<!DOCTYPE html>
<html lang="en">
<head>
<meta charset="utf-8">
<title>Brightwell.co business card</title>
<link href="https://fonts.googleapis.com/css2?family=Open+Sans:wght@400;600;700&display=swap" rel="stylesheet">
<style>
  :root {
    --orange: #ec7a1c;
    --orange-deep: #e0581f;
    --orange-light: #f39a2a;
    --ink: #2a2a2a;
    --ink-soft: #4a4a4a;
    --paper: #ffffff;
    --backdrop: #d9d9d9;
    --faint: #f0f0f0;
    --edge: #1e1e1e;
  }
  * { box-sizing: border-box; margin: 0; padding: 0; }
  html, body { width: 1200px; height: 852px; overflow: hidden; }
  body {
    background: var(--backdrop);
    font-family: "Open Sans", Arial, sans-serif;
    position: relative;
  }
  .card {
    position: absolute;
    width: 540px;
    height: 310px;
    border-radius: 14px;
    background: var(--paper);
    overflow: hidden;
    box-shadow: 0 6px 18px rgba(0,0,0,0.18);
  }

  /* ---------- Reverse: feelings & needs ---------- */
  .card-reverse { left: 90px; top: 90px; }
  .card-reverse .bottom-band {
    position: absolute; left: 0; right: 0; bottom: 0; height: 8px;
    background: var(--orange);
  }
  .card-reverse .faint-mark {
    position: absolute; left: 150px; top: 100px;
    font-size: 64px; font-weight: 700; color: var(--faint);
    letter-spacing: -1px;
  }
  .list-block { position: absolute; }
  .list-block h2 {
    color: var(--orange); font-size: 15px; font-weight: 700;
    letter-spacing: 0.5px; margin-bottom: 4px;
  }
  .list-columns { display: flex; gap: 18px; }
  .list-columns ul { list-style: none; }
  .list-columns li {
    font-size: 16px; line-height: 21px; color: var(--ink);
  }
  .list-columns li::before {
    content: "»"; color: var(--orange); font-weight: 700;
    margin-right: 8px;
  }
  .list-columns li.more::before { content: ""; margin-right: 17px; }
  .feelings { left: 34px; top: 120px; }
  .needs { left: 300px; top: 34px; }
  .divider {
    position: absolute; left: 282px; top: 40px; width: 2px; height: 130px;
    background: var(--orange);
  }

  /* ---------- Front: contact ---------- */
  .card-front { left: 570px; top: 462px; }
  .front-art { position: absolute; inset: 0; }
  .brand-mark {
    position: absolute; left: 40px; top: 132px;
    display: flex; align-items: center; gap: 10px;
    color: var(--paper); font-size: 24px; font-weight: 700;
  }
  .brand-mark .dot {
    width: 18px; height: 18px; border-radius: 50%; background: var(--paper);
  }
  .contact { position: absolute; left: 302px; top: 56px; }
  .contact .name {
    color: var(--orange); font-size: 18px; font-weight: 600; margin-bottom: 2px;
  }
  .contact .role {
    color: var(--ink-soft); font-size: 12px; line-height: 16px;
  }
  .contact-lines { list-style: none; margin-top: 42px; }
  .contact-lines li {
    display: flex; align-items: center; gap: 10px;
    font-size: 14px; line-height: 22px; color: var(--ink);
  }
  .contact-lines svg { width: 13px; height: 13px; fill: var(--orange); flex: none; }
</style>
</head>
<body>

  <section class="card card-reverse" aria-label="Card reverse: feelings and needs">
    <div class="faint-mark" aria-hidden="true">Brightwell.co</div>

    <div class="list-block feelings">
      <h2>FEELINGS</h2>
      <div class="list-columns">
        <ul>
          <li>confusion</li><li>curious</li><li>despair</li>
          <li>edgy</li><li>fiery</li><li>grief</li>
        </ul>
        <ul>
          <li>nervous</li><li>powerless</li><li>shock</li>
          <li>torn</li><li>weary</li><li class="more">&amp; more..</li>
        </ul>
      </div>
    </div>

    <div class="divider"></div>

    <div class="list-block needs">
      <h2>NEEDS</h2>
      <div class="list-columns">
        <ul>
          <li>belonging</li><li>choice</li><li>clarity</li>
          <li>empathy</li><li>freedom</li><li>meaning</li>
        </ul>
        <ul>
          <li>mourning</li><li>peace</li><li>safety</li>
          <li>support</li><li>understanding</li><li class="more">&amp; more</li>
        </ul>
      </div>
    </div>

    <div class="bottom-band"></div>
  </section>

  <section class="card card-front" aria-label="Card front: contact details">
    <svg class="front-art" viewBox="0 0 540 310" preserveAspectRatio="none" aria-hidden="true">
      <defs>
        <linearGradient id="front-gradient" x1="0" y1="0" x2="1" y2="1">
          <stop offset="0" stop-color="var(--orange-light)"/>
          <stop offset="0.6" stop-color="var(--orange)"/>
          <stop offset="1" stop-color="var(--orange-deep)"/>
        </linearGradient>
      </defs>
      <path d="M0 0 H250 C300 60 300 220 225 310 H0 Z" fill="url(#front-gradient)"/>
      <path d="M250 0 C300 60 300 220 225 310" fill="none" stroke="var(--edge)" stroke-width="4"/>
    </svg>

    <div class="brand-mark"><span class="dot"></span>Brightwell.co</div>

    <div class="contact">
      <p class="name">Marisabel T. Oberholt</p>
      <p class="role">MSc &amp; Certified Wellness Coach</p>
      <p class="role">Group Facilitator &amp; Coach</p>

      <ul class="contact-lines">
        <li>
          <svg viewBox="0 0 16 16"><path d="M4 0h8a1.5 1.5 0 0 1 1.5 1.5v13A1.5 1.5 0 0 1 12 16H4a1.5 1.5 0 0 1-1.5-1.5v-13A1.5 1.5 0 0 1 4 0zm0 2v10h8V2zm4 11a1 1 0 1 0 0 2 1 1 0 0 0 0-2z"/></svg>
          01632 960 418
        </li>
        <li>
          <svg viewBox="0 0 16 16"><path d="M1 5c0-2 3-3 7-3s7 1 7 3v1h-4V4.5H5V6H1zm2 2h10l1.5 7h-13zm5 1.5a2 2 0 1 0 0 4 2 2 0 0 0 0-4z"/></svg>
          07700 900 862
        </li>
        <li>
          <svg viewBox="0 0 16 16"><path d="M0 3h16v10H0zm1.5 1.3V12h13V4.3L8 9z M2 4l6 4.5L14 4z"/></svg>
          marisabel@brightwell-example.co
        </li>
        <li>
          <svg viewBox="0 0 16 16"><path d="M8 0a8 8 0 1 0 0 16A8 8 0 0 0 8 0zm0 1.5c1 1 1.8 3 2 5.7H6c.2-2.7 1-4.7 2-5.7zM1.6 7.2a6.5 6.5 0 0 1 3.6-5.1 10 10 0 0 0-1.2 5.1zm0 1.6H4a10 10 0 0 0 1.2 5.1 6.5 6.5 0 0 1-3.6-5.1zM8 14.5c-1-1-1.8-3-2-5.7h4c-.2 2.7-1 4.7-2 5.7zm2.8-.6A10 10 0 0 0 12 8.8h2.4a6.5 6.5 0 0 1-3.6 5.1zM12 7.2a10 10 0 0 0-1.2-5.1 6.5 6.5 0 0 1 3.6 5.1z"/></svg>
          www.brightwell-example.co
        </li>
      </ul>
    </div>
  </section>

</body>
</html>
```